Mobile Fitness snd Therapy Business Card Design

I need a business card designed for my mobile fitness and therapy business.

Please view the images that I have uploaded. I like the simplicity of the design that I have attached. I adapted it with my information

Target Market(s)

Those seeking personal training, injury rehabilitation or massage therapy.

Industry/Entity Type

Business

Contact Information for Business Card

Derek Holloway - MSc, CAT(C), RMT, CSCS, Pn2
e-mail: derek@bravuumfit.example
website: www.bravuumfit.example
instagram: @derek_holloway

Font styles to use
Sans Serif

Colors
3176b5
0355a3

Requirements
Must have
• "Contact us to receive a FREE assessment"
• Services offered:
• Personal Training
• Golf Fitness
• Injury Rehab
• Massage Therapy
• Yoga
Nice to have
• Consistent colours with brand
• - Dark Blue: #232837
• - Blue: #5096f0
• Consistent look/feel with the website: www.bravuumfit.example

```html
<!DOCTYPE html>
<html lang="en">
<head>
<meta charset="utf-8">
<title>Bravuum Business Card</title>
<link rel="stylesheet" href="https://fonts.googleapis.com/css2?family=Open+Sans:wght@400;600;800&display=swap">
<style>
  :root {
    --page: #9c9c9c;
    --card-blue: #2259a5;
    --light-blue: #3f7cbf;
    --brand-red: #ee2e2a;
    --ink-dark: #232837;
    --charcoal: #333336;
    --white: #ffffff;
  }
  html, body {
    margin: 0;
    padding: 0;
    width: 960px;
    height: 1200px;
    overflow: hidden;
    background: var(--page);
    font-family: "Open Sans", Arial, sans-serif;
  }
  .canvas {
    position: relative;
    width: 960px;
    height: 1200px;
  }
  .card {
    position: absolute;
    left: 26px;
    width: 906px;
    height: 548px;
    background: var(--card-blue);
    overflow: hidden;
    box-shadow: 2px 3px 4px rgba(0,0,0,0.35);
  }
  .card--front { top: 38px; }
  .card--back { top: 612px; }

  .brand {
    position: absolute;
    left: 0;
    width: 100%;
    text-align: center;
    color: var(--ink-dark);
  }
  .brand__name {
    margin: 0;
    font-weight: 800;
    font-size: 104px;
    line-height: 1;
    letter-spacing: 6px;
  }
  .brand__tagline {
    margin: 14px 0 0;
    font-weight: 800;
    font-size: 27px;
    letter-spacing: 6.5px;
  }
  .card--front .brand { top: 88px; }
  .card--back .brand { top: 150px; }

  .band {
    position: absolute;
    left: 0;
    bottom: 0;
    width: 100%;
  }
  .card--front .band { height: 234px; }
  .card--back .band { height: 120px; }

  .services {
    position: absolute;
    left: 64px;
    top: 318px;
    color: var(--white);
  }
  .services__title {
    margin: 0 0 10px;
    font-weight: 400;
    font-size: 33px;
    line-height: 1.2;
  }
  .services__list {
    list-style: none;
    margin: 0;
    padding: 0 0 0 40px;
    font-size: 19.5px;
    line-height: 30.4px;
  }

  .contact {
    position: absolute;
    left: 558px;
    top: 314px;
  }
  .contact__rail {
    position: absolute;
    left: 0;
    top: 0;
    width: 48px;
    height: 172px;
    background: var(--brand-red);
    border-radius: 0 0 24px 24px;
  }
  .contact__list {
    list-style: none;
    margin: 0;
    padding: 26px 0 0;
    color: var(--white);
    font-size: 21px;
  }
  .contact__item {
    display: flex;
    align-items: center;
    height: 37px;
    position: relative;
  }
  .contact__icon {
    width: 48px;
    display: flex;
    justify-content: center;
    position: relative;
    z-index: 1;
  }
  .contact__text { margin-left: 18px; }

  .offer {
    position: absolute;
    left: 37px;
    top: 428px;
    margin: 0;
    padding-top: 6px;
    color: var(--white);
    font-size: 22px;
    font-weight: 400;
  }
  .brand-dot {
    position: absolute;
    left: 660px;
    top: 460px;
    width: 40px;
    height: 40px;
    border-radius: 50%;
    background: #5096f0;
  }
</style>
</head>
<body>
<main class="canvas">

  <section class="card card--front" aria-label="Card front">
    <div class="brand">
      <h1 class="brand__name">BRAVUUM</h1>
      <p class="brand__tagline">NUTRITION - FITNESS - HEALTH</p>
    </div>

    <svg class="band" viewBox="0 0 906 234" preserveAspectRatio="none" aria-hidden="true">
      <path d="M557 0 H906 V234 H358 C358 110 430 20 557 0 Z" fill="var(--light-blue)"/>
      <path d="M0 0 H510 C420 22 348 110 346 234 H0 Z" fill="var(--brand-red)"/>
    </svg>

    <div class="services">
      <h2 class="services__title">Services offered:</h2>
      <ul class="services__list">
        <li>-Personal Training</li>
        <li>- Golf Fitness</li>
        <li>- Injury Rehab</li>
        <li>- Massage Therapy</li>
        <li>- Yoga</li>
      </ul>
    </div>

    <div class="contact">
      <div class="contact__rail"></div>
      <ul class="contact__list">
        <li class="contact__item">
          <span class="contact__icon">
            <svg width="26" height="26" viewBox="0 0 26 26" aria-hidden="true">
              <text x="13" y="21" text-anchor="middle" font-family="Open Sans, sans-serif" font-weight="800" font-size="25" fill="#fff">@</text>
            </svg>
          </span>
          <span class="contact__text">derek@bravuumfit.example</span>
        </li>
        <li class="contact__item">
          <span class="contact__icon">
            <svg width="24" height="24" viewBox="0 0 24 24" aria-hidden="true">
              <circle cx="12" cy="12" r="10" fill="none" stroke="#fff" stroke-width="2.4"/>
              <ellipse cx="12" cy="12" rx="4" ry="10" fill="none" stroke="#fff" stroke-width="2"/>
              <line x1="2" y1="12" x2="22" y2="12" stroke="#fff" stroke-width="2"/>
            </svg>
          </span>
          <span class="contact__text">www.bravuumfit.example</span>
        </li>
        <li class="contact__item">
          <span class="contact__icon">
            <svg width="24" height="24" viewBox="0 0 24 24" aria-hidden="true">
              <circle cx="12" cy="12" r="10" fill="none" stroke="#fff" stroke-width="2.6"/>
            </svg>
          </span>
          <span class="contact__text">@derek_holloway</span>
        </li>
      </ul>
    </div>
  </section>

  <section class="card card--back" aria-label="Card back">
    <div class="brand">
      <h2 class="brand__name">BRAVUUM</h2>
      <p class="brand__tagline">NUTRITION - FITNESS - HEALTH</p>
    </div>

    <svg class="band" viewBox="0 0 906 120" preserveAspectRatio="none" aria-hidden="true">
      <path d="M0 0 H520 C450 15 400 60 376 120 H0 Z" fill="var(--light-blue)"/>
      <path d="M550 0 H906 V120 H390 C418 55 470 12 550 0 Z" fill="var(--charcoal)"/>
    </svg>

    <p class="offer">Contact us to receive a FREE assessment</p>
    <div class="brand-dot"></div>
  </section>

</main>
</body>
</html>
```